Sorrel Flyer

My business is as owner and manager of 6 holiday lets in the South West of WA in the wine region.
All our properties are on rural bush locations, but close to all the amenitiies of the Tarrabellup township and major wineries in the area.
we advertise all the properties thru lodgio.com.au
you can check out the details of all the properties with the following links
www.lodgio.com.au/40217 Wattles Retreat..Max occ 16
www.lodgio.com.au/38562 Emberlight Retreat Max occ 8
www.lodgio.com.au/47390 Quokkas Corner Max occ 12
www.lodgio.com.au/82615 Bellintary Max occ 10
www.lodgio.com.au/120448 The Glade Retreat Max occ 8
www.lodgio.com.au/159026 Ferncliff Studio Max Occ 4
i am looking to produce a flyer that i can leave in all the houses to promote one to the other.
**I would like the flyer to be DL size (pls ignore the A5 mentioned above).
DL (99 x 210 mm) - Please download the templates below:
Photoshop - http://printnook.com.au/propath/download-template.aspx?Log=1&path=propath&pfid=BFB&pf_id=BFB&type=2
Illustrator - http://printnook.com.au/propath/download-template.aspx?Log=1&path=propath&pfid=BFB&pf_id=BFB&type=3
Thanks for all the submissions, but we are happy with one designer and just about to compete the process.
Target Market(s)
Family groups on holidays
Industry/Entity Type
Business
Requirements
Must have
- Photos and descriptions of all the houses.
Must have a feel of holidays in the wine region
You can get from the links I have given .
Also must have the logo and personal details as used on the business card

```html
<!DOCTYPE html>
<html lang="en">
<head>
<meta charset="utf-8">
<title>Sorrel Holidays Flyer</title>
<link rel="stylesheet" href="https://fonts.googleapis.com/css2?family=Libre+Baskerville:wght@700&family=Didact+Gothic&family=Lato:wght@400;700&display=swap">
<style>
  :root {
    --page: #ffffff;
    --ink: #1a1a1a;
    --band: rgba(52, 44, 36, 0.82);
    --olive: #b6a73c;
    --back-bg: #2c221e;
    --cream: #f2eee6;
    --caption: #d8d2c4;
  }
  * { box-sizing: border-box; margin: 0; padding: 0; }
  html, body { width: 1200px; height: 600px; overflow: hidden; background: var(--page); }
  .sheet { position: relative; width: 1200px; height: 600px; font-family: "Lato", sans-serif; }
  .side-label { position: absolute; top: 60px; font-family: "Lato", sans-serif; font-size: 30px; color: var(--ink); width: 200px; text-align: center; }
  .side-label--front { left: 180px; }
  .side-label--back { left: 803px; }

  /* Front */
  .front { position: absolute; left: 8px; top: 105px; width: 581px; height: 411px; overflow: hidden;
    background: linear-gradient(180deg, #9fb7d4 0%, #dfe6ee 14%, #cfd8dc 22%, #7d8a55 45%, #6b7a3c 60%, #8a8450 80%, #b7ae86 100%); }
  .front__headline { position: absolute; left: 27px; top: 27px; font-family: "Libre Baskerville", serif; font-weight: 700; font-size: 14.5px; line-height: 20px; color: #2a2a2a; }
  .brand { position: absolute; text-align: center; font-family: "Didact Gothic", sans-serif; color: #1e1e1e; }
  .brand__name { font-size: 38px; line-height: 38px; letter-spacing: 1px; }
  .brand__tag { font-size: 6.5px; letter-spacing: 0.3px; }
  .front .brand { left: 432px; top: 28px; width: 130px; }
  .row { position: absolute; left: 8px; width: 570px; background: var(--band); }
  .row--top { top: 80px; height: 120px; }
  .row--bottom { top: 247px; height: 133px; }
  .property { position: absolute; top: 0; width: 190px; height: 100%; }
  .property__name { position: absolute; left: 22px; top: 2px; font-family: "Libre Baskerville", serif; font-weight: 700; font-size: 11px; color: #fff; white-space: nowrap; }
  .property__photo { position: absolute; left: 6px; top: 18px; width: 122px; height: 88px; border: 2px solid var(--olive); }
  .row--bottom .property__photo { top: 23px; height: 90px; }
  .property__text { position: absolute; left: 131px; top: 18px; width: 54px; font-size: 5.4px; line-height: 7.2px; color: var(--cream); }
  .row--bottom .property__text { top: 23px; }
  .property__caption { position: absolute; left: 6px; top: 110px; width: 122px; text-align: center; font-style: italic; font-size: 4.8px; color: var(--caption); }
  .row--bottom .property__caption { top: 115px; }
  .photo--stone { background: linear-gradient(180deg, #c9d5de 0%, #8c6c4e 40%, #5e7a3a 70%, #6d8f3c 100%); }
  .photo--cottage { background: linear-gradient(180deg, #b9cde0 0%, #7c8a6a 40%, #7a6b45 65%, #5f7a36 100%); }
  .photo--barn { background: linear-gradient(180deg, #7fa9d8 0%, #e8e6df 40%, #a87a4a 60%, #8aa24e 100%); }
  .photo--verandah { background: linear-gradient(180deg, #6f9bd0 0%, #4f6b7a 40%, #6b8a3c 70%, #86a84a 100%); }
  .photo--deck { background: linear-gradient(180deg, #3b4a3c 0%, #5b4a38 45%, #8a6440 75%, #6e4e30 100%); }
  .photo--interior { background: linear-gradient(180deg, #7b5233 0%, #b58657 40%, #d9c8b0 70%, #8a7a6a 100%); }

  /* Back */
  .back { position: absolute; left: 607px; top: 105px; width: 581px; height: 411px; background: var(--back-bg); color: #fff; font-family: "Didact Gothic", sans-serif; }
  .back .brand { left: 425px; top: 28px; width: 130px; color: #fff; }
  .back__offer { position: absolute; left: 0; top: 132px; width: 100%; text-align: center; font-family: "Lato", sans-serif; font-size: 13.5px; line-height: 18px; letter-spacing: 0.2px; }
  .contact { position: absolute; top: 204px; font-size: 20px; letter-spacing: 1.5px; line-height: 22px; }
  .contact--left { left: 27px; }
  .contact--right { right: 45px; text-align: right; }
  .contact__phone { font-size: 14px; letter-spacing: 2px; margin-top: 2px; }
  .contact__mark { color: var(--olive); }
  .back__email { position: absolute; left: 0; top: 267px; width: 100%; text-align: center; font-size: 14px; letter-spacing: 1.8px; }
  .listings { position: absolute; top: 306px; left: 0; width: 100%; font-family: "Lato", sans-serif; font-size: 10.5px; line-height: 17px; }
  .listings__col { position: absolute; top: 0; }
  .listings__col--left { right: 296px; text-align: right; }
  .listings__col--right { left: 294px; }
  .listings__divider { position: absolute; left: 289px; top: 2px; width: 1px; height: 48px; background: #9a928a; }
  .listings__name { margin-right: 8px; }
</style>
</head>
<body>
<div class="sheet">
  <div class="side-label side-label--front">Front</div>
  <div class="side-label side-label--back">Back</div>

  <section class="front">
    <h1 class="front__headline">Contact us now to book<br>your perfect holiday in the wine region</h1>
    <div class="brand">
      <div class="brand__name">sorrel</div>
      <div class="brand__tag">wine country holiday homes</div>
    </div>

    <div class="row row--top">
      <article class="property" style="left:0">
        <h2 class="property__name">Wattles Retreat</h2>
        <div class="property__photo photo--stone" role="img" aria-label="Photo of a two-storey stone and timber home on a green lawn"></div>
        <p class="property__text">Wattles Retreat is a fabulous stone and timber family home with huge lounge areas, an upstairs loft, an open kitchen and a big dining space for everyone.</p>
        <p class="property__caption">6 Bedrooms, 3 Bathrooms, Sleeps up to 16</p>
      </article>
      <article class="property" style="left:190px">
        <h2 class="property__name">Emberlight Retreat</h2>
        <div class="property__photo photo--cottage" role="img" aria-label="Photo of a cottage with a verandah set in bushland"></div>
        <p class="property__text">Superbly quiet acre bush location. No neighbours in view. Only ten minutes to Tarrabellup for shopping, wineries and beaches. Kangaroos visit every afternoon.</p>
        <p class="property__caption">3 Bedrooms, 2 Bathrooms, Sleeps up to 8</p>
      </article>
      <article class="property" style="left:380px">
        <h2 class="property__name">Quokkas Corner</h2>
        <div class="property__photo photo--barn" role="img" aria-label="Photo of a timber holiday house under a blue sky"></div>
        <p class="property__text">Quokkas Corner is a fantastic holiday home only minutes to Tarrabellup and the beaches, set on bush acres ideal for large family groups.</p>
        <p class="property__caption">5 Bedrooms, 3 Bathrooms, Sleeps up to 12</p>
      </article>
    </div>

    <div class="row row--bottom">
      <article class="property" style="left:0">
        <h2 class="property__name">Bellintary Retreat</h2>
        <div class="property__photo photo--verandah" role="img" aria-label="Photo of a country house with a shaded verandah and lawn"></div>
        <p class="property__text">Bellintary is a relaxing country retreat in a quiet location on five acres, with shady verandahs, a wood fire and plenty of room for everyone.</p>
        <p class="property__caption">4 Bedrooms, 2 Bathrooms, Sleeps 8-10</p>
      </article>
      <article class="property" style="left:190px">
        <h2 class="property__name">The Glade Retreat</h2>
        <div class="property__photo photo--deck" role="img" aria-label="Photo of a timber deck with outdoor dining setting"></div>
        <p class="property__text">This family home is set on acres just around the corner from local galleries, with a big deck, outdoor dining and bush walks close by.</p>
        <p class="property__caption">4 Bedrooms, 3 Bathrooms, Sleeps 8 adults</p>
      </article>
      <article class="property" style="left:380px">
        <h2 class="property__name">Ferncliff Studio</h2>
        <div class="property__photo photo--interior" role="img" aria-label="Photo of an open living room under a timber ceiling"></div>
        <p class="property__text">Ferncliff Studio is a rustic two bedroom cottage set amongst tall trees, secluded and peaceful, yet only minutes from vineyards and cafes.</p>
        <p class="property__caption">2 Bedrooms, 1 Bathroom, Sleeps up to 4</p>
      </article>
    </div>
  </section>

  <section class="back">
    <div class="brand">
      <div class="brand__name">sorrel</div>
      <div class="brand__tag">wine country holiday homes</div>
    </div>
    <p class="back__offer">IF YOU'RE LOOKING FOR A LAST MINUTE BOOKING.....<br>MAKE US AN OFFER. WE DONT LIKE SEEING THE HOUSE EMPTY</p>
    <div class="contact contact--left">
      <div>Marcus Delaney</div>
      <div class="contact__phone"><span class="contact__mark">M.</span>0400 555 181</div>
    </div>
    <div class="contact contact--right">
      <div>Joanne Jarvis</div>
      <div class="contact__phone"><span class="contact__mark">M.</span>0400 555 272</div>
    </div>
    <p class="back__email"><span class="contact__mark">E.</span> hello@sorrelholidays.com.au</p>
    <div class="listings">
      <div class="listings__col listings__col--left">
        <div><span class="listings__name">Wattles Retreat</span>www.lodgio.com.au/40217</div>
        <div><span class="listings__name">Emberlight Retreat</span>www.lodgio.com.au/38562</div>
        <div><span class="listings__name">Quokkas Corner</span>www.lodgio.com.au/47390</div>
      </div>
      <div class="listings__divider"></div>
      <div class="listings__col listings__col--right">
        <div><span class="listings__name">Bellintary</span>www.lodgio.com.au/82615</div>
        <div><span class="listings__name">The Glade Retreat</span>www.lodgio.com.au/120448</div>
        <div><span class="listings__name">Ferncliff Studio</span>www.lodgio.com.au/159026</div>
      </div>
    </div>
  </section>
</div>
</body>
</html>
```